IT Company seeking creative modern BUSINESS CARD DESIGN!

We are a full service IT company located in California. We specialize in offering computer network support to small to medium to enterprise sized businesses. We are looking for a new business card design to go with our newly designed logo. We prefer business cards that are unique and make a lasting impression. We tend to like business cards with black, gray or blue backgrounds. Our color theme should include black, blue, gray and white only. We want something BOLD, BRIGHT, FUN, CLEAN, and MODERN. Please design with creativity in mind! :) We want our business cards to "pop" and "stand out" when compared to other business cards side by side. We want to be different and make that WINNING first impression every time!! =)

FONT NAME FOR harbor forge is "Cynthe" True Type font.

BLUE LOGO COLOR IS:
Hex: #2375BB
R: 35
G: 117
B: 187

The secondary color is pure "Black". Use of Grayscale is okay too.
Updates

Please look over the sample designs I attached. ** IMPORTANT ** This will give you an idea of the color, design and layouts we like. Also, our logo needs to stand out (nothing small and DO NOT duplicate logo twice on same side of the card. We do want a front and back to the card design. You are welcome to separate the circle logo and the business name if needed. Also, please no pastel colors or busy backgrounds with design. Watermark backgrounds would be okay if it works with the logo design. Let me know if you have any issues opening the logo or font file. Thanks a bunch! EXCITED and AWAITING your designs! I will provide as much feedback as possible. Thank you, Tova :)

Target Market(s)

Small, Medium to Enterprise businesses. Business Card will be given to professionals. We want the card to stand out and look and feel different.

Industry/Entity Type

Computer

Font styles to use
Sans Serif

Colors
0555a3
ffffff
000000
474747
959595
5c5c5c
c8c8c8
eeeeee
3276b5

Requirements
Must have
• WE WANT TO STAND OUT! BE DIFFERENT! MAKE A LASTING IMPRESSION!

We like clean, neat, modern, BOLD look. See attachment for samples of designs we like.

This is the information needed on the business card. Exact information will change per employee (of course), but heres the required data needed (this info can go on either the front or back of the business card).

Business Logo (File attached)

Gary Loftis
CEO / Senior Network Engineer
7381 Delacroix Avenue
Suite D
Ashvale, CA 95871

main tel: 209-555-0172
direct tel: 209-555-0139
cell: 209-555-0186
fax tel: 209-xxx-xxxx

gloftis@hfqx.example
www.hfqx.example

We really like the use of icons for the address, phone, location etc. Looks modern and clean.

Nice to have
• Somewhere it would be nice to include the cities we are located in and serving:
Ashvale - Vellan - Kelderon - Brightmoor (FYI - if there's no design space to include these cities, then that's okay. This is just a wish list item to include if theres room. =)

We like watermark background effects if that's an option. Not necessary though.

If there's a way to include we are on Face Book, Linked In, and Twitter - that would be cool, but not necessary.

Different Card Size or cut ot rounded edges might be cool, but not necessary. We do want to STAND OUT and be different.
Should not have
• No other colors other than Blue, Black, Gray, White. Do not like pastel blue or light blue. For lighter coloring.... would prefer gray scale or white. Keep BLUE color bold and vibrant (like samples I attached).

Do not do a traditional white business card. Too boring and ordinary. Do not make address and phone information in large fat fonts. We want neat and tidy - modern looking fonts. :)

```html
<!DOCTYPE html>
<html lang="en">
<head>
<meta charset="utf-8">
<title>harbor forge – business card</title>
<link rel="stylesheet" href="https://fonts.googleapis.com/css2?family=Arimo:wght@400;700&family=Roboto+Condensed:wght@700&display=swap">
<style>
  :root {
    --brand-blue: #2375bb;
    --ink: #2b2b2b;
    --edge: #1e1e1e;
    --paper: #ffffff;
    --text: #222222;
  }
  * { box-sizing: border-box; margin: 0; padding: 0; }
  html, body { width: 1200px; height: 974px; overflow: hidden; background: var(--paper); }
  body { position: relative; font-family: "Arimo", Arial, sans-serif; color: var(--text); }

  .card {
    position: absolute; top: 42px; width: 522px; height: 890px;
    background: var(--brand-blue); border: 2px solid var(--edge); overflow: hidden;
  }
  .card--front { left: 53px; }
  .card--back { left: 626px; }

  .brand { position: absolute; left: 0; width: 100%; text-align: center; }
  .brand__mark {
    position: absolute; width: 94px; height: 94px; border-radius: 50%;
    background: var(--paper); left: 50%; transform: translateX(-50%);
  }
  .brand__name {
    position: absolute; left: 0; width: 100%; text-align: center;
    font-family: "Arimo", Arial, sans-serif; font-weight: 700; font-size: 46px;
    color: var(--paper); letter-spacing: 1px;
  }
  .card--front .brand__mark { top: 40px; }
  .card--front .brand__name { top: 160px; }
  .card--back .brand__mark { top: 311px; }
  .card--back .brand__name { top: 425px; }

  .info-panel {
    position: absolute; left: 53px; top: 266px; width: 412px; height: 640px;
    background: var(--paper); border-radius: 45px 45px 0 0;
  }

  .name-plate {
    position: absolute; left: 78px; top: 321px; width: 362px; height: 82px;
    background: var(--ink); border-radius: 30px; color: var(--paper);
    display: flex; flex-direction: column; align-items: center; justify-content: center;
    font-family: "Roboto Condensed", "Arial Narrow", sans-serif; font-weight: 700;
  }
  .name-plate__name { font-size: 31px; line-height: 34px; padding-top: 4px; }
  .name-plate__title { font-size: 18px; line-height: 20px; }

  .divider-bar {
    position: absolute; left: 78px; width: 362px; height: 41px;
    background: var(--ink); border-radius: 10px;
  }
  .divider-bar--phones { top: 552px; }
  .divider-bar--address { top: 735px; }

  .icon-badge {
    position: absolute; width: 52px; height: 52px; border-radius: 50%;
    background: var(--ink); display: flex; align-items: center; justify-content: center;
  }
  .icon-badge svg { width: 28px; height: 28px; fill: var(--paper); }

  .phone-list { position: absolute; left: 92px; top: 447px; font-size: 19px; line-height: 24px; }
  .phone-list .label { color: var(--brand-blue); }

  .web-line { position: absolute; right: 85px; font-size: 19px; line-height: 24px; text-align: right; }
  .web-line--email { top: 632px; }
  .web-line--site { top: 677px; }

  .address { position: absolute; left: 92px; top: 815px; font-size: 19px; line-height: 24px; }

  .locations-band {
    position: absolute; left: 0; bottom: 0; width: 100%; height: 70px;
    background: var(--ink); color: var(--paper);
    display: flex; align-items: center; justify-content: center; padding-top: 6px;
    font-weight: 700; font-size: 20px; gap: 8px;
  }
  .locations-band .dot { color: var(--brand-blue); font-size: 16px; }
</style>
</head>
<body>

<section class="card card--front">
  <div class="brand">
    <div class="brand__mark"></div>
    <div class="brand__name">harbor forge</div>
  </div>

  <div class="info-panel"></div>

  <div class="name-plate">
    <span class="name-plate__name">Gary Loftis</span>
    <span class="name-plate__title">President / CEO</span>
  </div>
  <div class="icon-badge" style="left:233px; top:285px;">
    <svg viewBox="0 0 24 24"><circle cx="12" cy="8" r="5"/><path d="M3 23c0-5 4-8 9-8s9 3 9 8z"/></svg>
  </div>

  <div class="phone-list">
    <div>209.555.0172 <span class="label">Help Desk</span></div>
    <div>209.555.0139 <span class="label">Direct</span></div>
    <div>209.555.0186 <span class="label">Cell</span></div>
  </div>

  <div class="divider-bar divider-bar--phones"></div>
  <div class="icon-badge" style="left:98px; top:520px;">
    <svg viewBox="0 0 24 24"><path d="M2 8c0-3 4-5 10-5s10 2 10 5v2h-5V8H7v2H2z"/><path d="M5 12h14l2 9H3z"/><rect x="8" y="13" width="8" height="6" fill="#2b2b2b"/></svg>
  </div>
  <div class="icon-badge" style="left:368px; top:573px;">
    <svg viewBox="0 0 24 24"><path d="M12 2a10 10 0 1 0 0 20 10 10 0 0 0 0-20zm0 2c1.3 1.5 2.2 3.6 2.4 7H9.6c.2-3.4 1.1-5.5 2.4-7zM9.7 4.6C8.3 6.3 7.7 8.5 7.6 11H4.1a8 8 0 0 1 5.6-6.4zm4.6 0A8 8 0 0 1 19.9 11h-3.5c-.1-2.5-.7-4.7-2.1-6.4zM4.1 13h3.5c.1 2.5.7 4.7 2.1 6.4A8 8 0 0 1 4.1 13zm5.5 0h4.8c-.2 3.4-1.1 5.5-2.4 7-1.3-1.5-2.2-3.6-2.4-7zm6.8 0h3.5a8 8 0 0 1-5.6 6.4c1.4-1.7 2-3.900 2.1-6.4z"/></svg>
  </div>

  <div class="web-line web-line--email">gloftis@hfqx.example</div>
  <div class="web-line web-line--site">www.hfqx.example</div>

  <div class="divider-bar divider-bar--address"></div>
  <div class="icon-badge" style="left:368px; top:702px;">
    <svg viewBox="0 0 24 24"><path d="M2 5h20v14H2z"/><path d="M2 5l10 8 10-8M2 19l7-7M22 19l-7-7" stroke="#2b2b2b" stroke-width="1.6" fill="none"/></svg>
  </div>
  <div class="icon-badge" style="left:98px; top:759px;">
    <svg viewBox="0 0 24 24"><path d="M12 3l10 9h-3v9h-5v-6h-4v6H5v-9H2z"/></svg>
  </div>

  <div class="address">
    <div>7381 Delacroix Avenue, Suite D</div>
    <div>Ashvale, CA 95871</div>
  </div>
</section>

<section class="card card--back">
  <div class="brand">
    <div class="brand__mark"></div>
    <div class="brand__name">harbor forge</div>
  </div>

  <div class="locations-band">
    <span>Ashvale</span><span class="dot">●</span>
    <span>Kelderon</span><span class="dot">●</span>
    <span>Vellan</span><span class="dot">●</span>
    <span>Brightmoor</span>
  </div>
  <div class="icon-badge" style="left:232px; top:785px;">
    <svg viewBox="0 0 24 24"><path d="M6 3h12v18H6z"/><path d="M3 21h18v1H3z"/><g fill="#2b2b2b"><rect x="8" y="5" width="2" height="2"/><rect x="11" y="5" width="2" height="2"/><rect x="14" y="5" width="2" height="2"/><rect x="8" y="9" width="2" height="2"/><rect x="11" y="9" width="2" height="2"/><rect x="14" y="9" width="2" height="2"/><rect x="8" y="13" width="2" height="2"/><rect x="11" y="13" width="2" height="2"/><rect x="14" y="13" width="2" height="2"/><rect x="10.5" y="17" width="3" height="4"/></g></svg>
  </div>
</section>

</body>
</html>
```